Business Card Design Project

We require a business card template to cover basic contact information - our company logo, names of employees, title, mobile and email.

Target Market(s)

Corporate

Industry/Entity Type

Business

Font styles to use
Sans Serif

Requirements
Nice to have
• Thinking it would be great just to have the logo taking up approximately half the space (so it goes as far across the top of the card as possible) and then contact details in the lower half of the card. Keen just to use only the two colours in the logo, on a white background.
Should not have
• No fussy drawings

```html
<!DOCTYPE html>
<html lang="en">
<head>
<meta charset="utf-8">
<title>Tidewell Developments – Business Card</title>
<link rel="stylesheet" href="https://fonts.googleapis.com/css2?family=Open+Sans:wght@400;600;700&display=swap">
<style>
  :root {
    --teal: #35a6b9;
    --blue: #3068aa;
    --ink: #444444;
    --icon: #3a3a3a;
    --card-light: #f5f5f5;
    --card-dark: #e8e8e8;
    --white: #ffffff;
  }
  * { margin: 0; padding: 0; box-sizing: border-box; }
  html, body {
    width: 1200px;
    height: 720px;
    overflow: hidden;
    background: var(--card-dark);
  }
  .card {
    position: relative;
    width: 1200px;
    height: 720px;
    overflow: hidden;
    background: radial-gradient(ellipse at 45% 25%, var(--card-light) 0%, #efefef 55%, var(--card-dark) 100%);
    font-family: "Open Sans", Arial, sans-serif;
  }
  .brand {
    position: absolute;
    left: 355px;
    top: 58px;
    width: 536px;
    color: var(--teal);
    font-weight: 600;
    text-align: right;
  }
  .brand-name {
    display: block;
    font-size: 118px;
    line-height: 140px;
    letter-spacing: -3px;
    text-align: left;
  }
  .brand-line {
    display: block;
    font-size: 30px;
    line-height: 36px;
    margin-top: -6px;
  }
  .band {
    position: absolute;
    left: 0;
    width: 1200px;
    color: var(--white);
    text-align: center;
    padding-left: 44px;
  }
  .band-name {
    top: 287px;
    height: 61px;
    background: var(--teal);
    font-size: 46px;
    font-weight: 700;
    line-height: 61px;
  }
  .band-title {
    top: 365px;
    height: 62px;
    background: var(--blue);
    font-size: 29px;
    font-weight: 400;
    line-height: 62px;
    padding-left: -28px;
  }
  .contact {
    position: absolute;
    display: flex;
    align-items: center;
    color: var(--ink);
    font-size: 26px;
    font-weight: 700;
    white-space: nowrap;
  }
  .contact svg { flex: none; fill: var(--icon); }
  .contact-phone { left: 100px; top: 464px; gap: 30px; }
  .contact-email { left: 96px; top: 586px; gap: 28px; }
  .contact-address { left: 765px; top: 456px; gap: 18px; }
  .contact-web { left: 764px; top: 588px; gap: 23px; }
  .at-sign { font-size: 30px; color: var(--icon); width: 30px; text-align: center; }
</style>
</head>
<body>
  <div class="card">
    <div class="brand">
      <span class="brand-name">Tidewell</span>
      <span class="brand-line">developments</span>
    </div>

    <div class="band band-name">Emp Name</div>
    <div class="band band-title">Title</div>

    <div class="contact contact-phone">
      <svg width="22" height="38" viewBox="0 0 22 38" aria-hidden="true">
        <path d="M3 0h16a3 3 0 0 1 3 3v32a3 3 0 0 1-3 3H3a3 3 0 0 1-3-3V3a3 3 0 0 1 3-3zm1 4v26h14V4z"/>
        <circle cx="11" cy="34" r="1.6" fill="var(--card-light)"/>
      </svg>
      <span>+123 156789</span>
    </div>

    <div class="contact contact-email">
      <span class="at-sign">@</span>
      <span>name@tidewell.com</span>
    </div>

    <div class="contact contact-address">
      <svg width="36" height="36" viewBox="0 0 36 36" aria-hidden="true">
        <path d="M18 1 0 18h5v17h10V24h6v11h10V18h5L29 11.4V3h-5v3.7z"/>
      </svg>
      <span>Address</span>
    </div>

    <div class="contact contact-web">
      <svg width="36" height="34" viewBox="0 0 36 34" aria-hidden="true">
        <path d="M2 0h32a2 2 0 0 1 2 2v22a2 2 0 0 1-2 2H2a2 2 0 0 1-2-2V2a2 2 0 0 1 2-2zm2 4v18h28V4z"/>
        <path d="M13 26h10l2 5h4v3H7v-3h4z"/>
      </svg>
      <span>www.tidewell.com</span>
    </div>
  </div>
</body>
</html>
```